Simple, Professional and neat business card design for Vendralo Inc.

We're looking to re-vamp our business card design. We're a supplier of innovative feed ingredients for the North American animal agriculture industry. We are located in Lucknow, Ontario, Canada and our flagship product is a product that prevents milk fever in dairy cows when the calve, it is fed before calving and is very effective compared to other alternatives available on the market today.

Our company has Danish roots and we import all of our product from our Danish partner/manufacturer in Denmark. We like our design to embrace high professionalism while remaining neat and simple.

Target Market(s)

B2B, Feed Mills, Veterinary Clinics, Large integrators/producers,

Industry/Entity Type

Agribusiness

Contact Information for Business Card

We like the rounded corners because they make the card easy to sit in a wallet and not many use it so it makes the card stand out, just possibly something to take account for during the design.

As you can also see on the sliders below, looking for a that simple but proffesional scandinavian design.

Requirements
Nice to have
• Rounded corners
Should not have
• Too vibrant

```html
<!DOCTYPE html>
<html lang="en">
<head>
<meta charset="utf-8">
<title>Vendralo Inc. – Business Card</title>
<link href="https://fonts.googleapis.com/css2?family=Montserrat:wght@400;500;700;800&display=swap" rel="stylesheet">
<style>
  :root {
    --blue: #1557a8;
    --blue-deep: #0f4590;
    --blue-light: #2a72c4;
    --gold: #d9bd82;
    --ink: #3a3a3a;
    --paper: #ffffff;
    --backdrop: #e9ebee;
  }
  * { box-sizing: border-box; margin: 0; padding: 0; }
  html, body {
    width: 1200px; height: 896px; overflow: hidden;
    background: var(--backdrop);
    font-family: "Montserrat", Arial, sans-serif;
  }
  .sheet {
    position: relative; width: 1200px; height: 896px;
    display: flex; justify-content: center; align-items: center; gap: 80px;
  }
  .card {
    position: relative; width: 340px; height: 560px;
    border-radius: 28px; overflow: hidden;
    box-shadow: 0 14px 34px rgba(0,0,0,.18);
  }
  /* Back side */
  .card-back {
    background: linear-gradient(160deg, var(--blue-light) 0%, var(--blue) 45%, var(--blue-deep) 100%);
    color: var(--paper);
  }
  .back-brand {
    position: absolute; top: 210px; left: 0; right: 0;
    display: flex; flex-direction: column; align-items: center; gap: 18px;
  }
  .brand-mark {
    width: 70px; height: 70px; border-radius: 50%;
    background: var(--gold);
  }
  .back-brand .brand-name {
    font-weight: 800; font-size: 26px; letter-spacing: .5px; color: var(--paper);
  }
  .back-web {
    position: absolute; bottom: 40px; left: 36px;
    font-size: 14px; letter-spacing: .6px; color: var(--paper);
  }
  /* Front side */
  .card-front { background: var(--paper); color: var(--ink); }
  .front-brand {
    position: absolute; top: 40px; right: 30px;
    display: flex; align-items: center; gap: 12px;
  }
  .front-brand .brand-square {
    width: 26px; height: 26px; background: var(--blue); border-radius: 4px;
  }
  .front-brand .brand-name {
    font-weight: 800; font-size: 22px; color: var(--blue); letter-spacing: .3px;
  }
  .person {
    position: absolute; top: 150px; right: 30px; text-align: right;
  }
  .person-name {
    font-weight: 500; font-size: 24px; letter-spacing: 1.5px; color: var(--blue);
    text-transform: uppercase;
  }
  .person-title { font-size: 13px; letter-spacing: .6px; margin-top: 2px; }
  .divider {
    position: absolute; top: 232px; right: 30px; width: 200px; height: 2px;
    background: linear-gradient(90deg, transparent, var(--blue));
  }
  .contact {
    position: absolute; top: 260px; left: 30px; right: 30px;
    font-size: 13.5px; line-height: 1.65; letter-spacing: .4px;
  }
  .address { margin-bottom: 6px; }
  .contact-row .label { color: var(--blue); font-weight: 500; margin-right: 4px; }
  .contact-row .accent { color: var(--blue); font-weight: 500; }
  .contact-divider {
    margin-top: 12px; width: 200px; height: 1px;
    background: linear-gradient(90deg, var(--blue), transparent);
  }
  .footer-band {
    position: absolute; left: 0; right: 0; bottom: 0; height: 64px;
    background: linear-gradient(160deg, var(--blue-light), var(--blue-deep));
    border-top: 4px solid var(--paper);
    box-shadow: 0 -2px 0 var(--gold);
  }
</style>
</head>
<body>
  <main class="sheet">
    <section class="card card-back" aria-label="Card back">
      <div class="back-brand">
        <span class="brand-mark"></span>
        <span class="brand-name">VENDRALO INC.</span>
      </div>
      <p class="back-web">www.vendralo.com</p>
    </section>

    <section class="card card-front" aria-label="Card front">
      <div class="front-brand">
        <span class="brand-square"></span>
        <span class="brand-name">VENDRALO INC.</span>
      </div>
      <div class="person">
        <h1 class="person-name">Anders Holm</h1>
        <p class="person-title">Director</p>
      </div>
      <div class="divider"></div>
      <div class="contact">
        <p class="address">Box 574, Ashbury,<br>Ontario Canada N0X 1R4</p>
        <p class="contact-row"><span class="label">M :</span>555-310-4471</p>
        <p class="contact-row"><span class="label">P :</span>555-310-4472</p>
        <p class="contact-row"><span class="label">T :</span>888-555-0147 (toll Free)</p>
        <p class="contact-row"><span class="label">F :</span>555-310-4479</p>
        <p class="contact-row"><span class="label">E :</span>anders@vendralo.com</p>
        <p class="contact-row"><span class="label">W :</span>www.<span class="accent">vendralo</span>.com</p>
        <div class="contact-divider"></div>
      </div>
      <div class="footer-band"></div>
    </section>
  </main>
</body>
</html>
```